Young Accounting firm needing a captivating business card

We need a business card design that forces the person to look at the card because its either gold foil, plastic, or lettering pop up etc. We already have a logo with a specific gold color and we need to make it pop. We are an accounting firm. I need the words" accounting, payroll, licenses, audits, taxes" somewhere on the business card so as to describe what we do- preferably on the side where the logo is at.

Industry/Entity Type

Accounting

Contact Information for Business Card

Address 48276 9th Ave S Ste 305, Federal Way, WA 98117
Business Phone (360)418-2096
Fax (360)418-2157
Office Cell Phone (360)586-7319

Font styles to use
Serif

Colors
85abd2

Requirements
Must have
• It should state
• "Accounting" "Taxes" "Audits" "Licenses" "Payroll"
Nice to have
• Matte with gold foil, different textures, With Either a textured ivory background or gray blue slate background
Should not have
• colorful colors

```html
<!DOCTYPE html>
<html lang="en">
<head>
<meta charset="utf-8">
<title>Tallywick Business Card</title>
<link href="https://fonts.googleapis.com/css2?family=Questrial&display=swap" rel="stylesheet">
<style>
  :root {
    --page: #cfd2d5;
    --card: #0a0a09;
    --pattern-a: #131311;
    --pattern-b: #080807;
    --gold-deep: #94700a;
    --gold: #c9a20c;
    --gold-bright: #f8f46a;
    --gold-text: #c8a412;
    --ink-light: #f2f2f2;
  }
  * { margin: 0; padding: 0; box-sizing: border-box; }
  html, body { width: 848px; height: 1200px; overflow: hidden; }
  body {
    background: var(--page);
    font-family: "Questrial", sans-serif;
    position: relative;
  }
  .card {
    position: absolute;
    left: 77px;
    width: 691px;
    height: 429px;
    background: var(--card);
    overflow: hidden;
  }
  .card--front { top: 85px; }
  .card--back { top: 625px; }
  .card__texture {
    position: absolute; inset: 0;
    background: radial-gradient(ellipse at 50% 40%, var(--pattern-a), var(--pattern-b));
  }
  .gold-tab {
    position: absolute;
    top: 0; left: 241px;
    width: 202px; height: 25px;
    clip-path: polygon(0 0, 100% 0, 93% 100%, 7% 100%);
    background: linear-gradient(90deg, var(--gold), var(--gold-deep) 40%, var(--gold-bright) 60%, var(--gold-deep) 90%);
  }
  .gold-band {
    position: absolute;
    left: 0; bottom: 0;
    width: 100%; height: 45px;
    background: linear-gradient(90deg, var(--gold) 0%, var(--gold-deep) 30%, var(--gold) 48%, var(--gold-bright) 56%, var(--gold) 80%, var(--gold-deep) 100%);
  }
  .brand-name {
    position: absolute;
    color: var(--gold-text);
    font-size: 64px;
    letter-spacing: -1px;
    line-height: 1;
    white-space: nowrap;
  }
  .card--front .brand-name { left: 0; width: 100%; text-align: center; top: 216px; }
  .card--back .brand-name { left: 44px; top: 222px; }
  .services {
    position: absolute;
    top: 338px; left: 0;
    width: 100%; height: 36px;
    list-style: none;
    font-size: 27px;
    line-height: 1.2;
    color: var(--gold-text);
    z-index: 2;
  }
  .services li { position: absolute; top: 0; white-space: nowrap; }
  .contact {
    position: absolute;
    color: var(--ink-light);
    font-size: 13.5px;
    line-height: 17px;
  }
  .contact__icon {
    position: absolute;
    left: 468px;
    width: 20px; height: 20px;
    fill: none; stroke: var(--ink-light); stroke-width: 1.6;
  }
  .contact__text {
    position: absolute;
    right: 30px;
    text-align: right;
    white-space: nowrap;
  }
</style>
</head>
<body>
  <section class="card card--front">
    <div class="card__texture" role="img" aria-label="Faint dark damask pattern"></div>
    <div class="gold-tab"></div>
    <div class="brand-name">Tallywick</div>
    <ul class="services">
      <li style="left:48px">Audits</li>
      <li style="left:157px">Taxes</li>
      <li style="left:258px">Licences</li>
      <li style="left:397px">Accounting</li>
      <li style="left:563px">Payroll</li>
    </ul>
    <div class="gold-band"></div>
  </section>

  <section class="card card--back">
    <div class="card__texture" role="img" aria-label="Faint dark damask pattern"></div>
    <div class="gold-tab"></div>
    <div class="brand-name">Tallywick</div>

    <svg class="contact__icon" style="top:151px" viewBox="0 0 20 20" aria-hidden="true">
      <path d="M2 9 L10 2 L18 9"/><path d="M4 8 V18 H16 V8"/><rect x="6" y="11" width="3" height="3"/><rect x="11" y="11" width="3" height="7"/>
    </svg>
    <div class="contact contact__text" style="top:153px">48276 9th Ave S Ste 305<br>Federal Way, WA 98117</div>

    <svg class="contact__icon" style="top:213px" viewBox="0 0 20 20" aria-hidden="true">
      <rect x="1.5" y="1.5" width="17" height="17" rx="3" fill="var(--ink-light)" stroke="none"/>
      <path d="M7 5 C5 7 6 12 10 15 L12 13 L10 11 L9 12 C8 10 8 9 8 8 L9 7 Z" fill="var(--card)" stroke="none"/>
    </svg>
    <div class="contact contact__text" style="top:215px">(360)&nbsp; 418-2096</div>
    <div class="contact contact__text" style="top:238px">(360)&nbsp; 418-2157</div>

    <svg class="contact__icon" style="top:277px" viewBox="0 0 20 20" aria-hidden="true">
      <path d="M2 8 C2 4 18 4 18 8 L15 9 L14 7 H6 L5 9 Z" fill="var(--ink-light)" stroke="none"/>
      <path d="M5 10 H15 L17 17 H3 Z" fill="var(--ink-light)" stroke="none"/>
      <circle cx="10" cy="13" r="2" fill="var(--card)" stroke="none"/>
    </svg>
    <div class="contact contact__text" style="top:280px">(360)&nbsp; 586-7319</div>

    <div class="gold-band"></div>
  </section>
</body>
</html>
```